Lease-My-Goose's web page

I need a web page(s) to show and promote my business of renting chickens. We provide seasonal rentals in the United States of a layer hen package for people who would like to try raising their own chickens. The package includes two hens, coop, attached run, feeder, waterer, and food. I would like interested people to be able to fill out a form so that I can have partners contact them to set up a delivery in their area. Our service is very popular with urban and suburban families.

Target Market(s)

Urban foodies.
Families.
People interested in Organic Foods.
People concerned with where their food comes from and how it is grown/prepared.
People interested in Urban Farming.

Industry/Entity Type

Business

Requirements
Must have
• A way for me to see rental interest based on zip code.
• A contact form including zip code, e-mail, and optional phone number.
• Our Logo. (Please contact if you are unable to use the file I provided.)
Nice to have
• A guest book for former renters that we can vet before posting.

```html
<!DOCTYPE html>
<html lang="en">
<head>
<meta charset="utf-8">
<title>Lease-My-Goose</title>
<link rel="stylesheet" href="https://fonts.googleapis.com/css2?family=Open+Sans:wght@400;600&display=swap">
<style>
:root{
  --green:#b2d235;
  --green-dark:#8fae1f;
  --olive:#6e8a1c;
  --text:#555;
  --muted:#777;
  --line:#cfcfcf;
  --panel:#eeeeee;
  --bg:#f4f4f4;
  --white:#fff;
}
*{box-sizing:border-box;margin:0;padding:0}
html,body{width:823px;height:1200px;overflow:hidden;background:var(--bg)}
body{font-family:"Open Sans",sans-serif;color:var(--text)}
.page{position:relative;width:960px;height:1400px;transform:scale(0.857143);transform-origin:0 0;background:linear-gradient(#f7f7f7,#efefef)}
.abs{position:absolute}

.topbar{right:14px;top:9px;font-size:14px;color:var(--muted);display:flex;align-items:center;gap:6px}
.social{width:17px;height:17px;border-radius:3px;display:inline-block}
.social.a{background:#3b5a9a}.social.b{background:#3aa7e0}

.nav{left:0;top:38px;width:960px;height:45px;background:linear-gradient(#f2f2f2,#e4e4e4);border-top:2px solid var(--green-dark);border-bottom:2px solid var(--green-dark)}
.nav a{position:absolute;top:11px;font-size:15px;color:var(--olive);text-decoration:none}
.nav .home{left:135px;top:8px;width:78px;height:24px;background:var(--green);border:1px solid var(--green-dark);color:var(--white);text-align:center;line-height:22px}
.search{left:728px;top:8px;width:218px;height:25px;background:var(--green);border-radius:3px;color:var(--white);font-size:15px;padding-left:10px;line-height:25px}
.search svg{position:absolute;right:9px;top:4px}

.logo{left:12px;top:12px;width:118px;height:92px;display:flex;flex-direction:column;align-items:center;justify-content:center;gap:4px}
.logo .dot{width:52px;height:52px;border-radius:50%;background:var(--green);border:3px solid var(--white)}
.logo .name{font-size:13px;font-weight:600;color:#c8291e}

.hero{left:0;top:120px;width:960px;height:350px;background:linear-gradient(100deg,#7f8a5a 0%,#9c9a72 35%,#55504d 60%,#6d6a58 100%)}
.hero h1{position:absolute;left:78px;top:90px;font-weight:400;font-size:38px;line-height:44px;color:var(--white)}
.hero p{position:absolute;left:81px;top:191px;font-size:18px;line-height:21px;color:var(--white)}
.readmore{position:absolute;left:81px;top:260px;width:139px;height:39px;border:2px solid var(--white);color:var(--white);font-size:18px;line-height:35px;padding-left:12px}
.readmore svg{position:absolute;right:14px;top:12px}
.arrow{position:absolute;top:151px;width:50px;height:50px;background:var(--white);opacity:.92}
.arrow.l{left:0;border-radius:0 6px 6px 0}.arrow.r{right:0;border-radius:6px 0 0 6px}
.arrow svg{position:absolute;left:14px;top:12px}
.progress{position:absolute;left:10px;top:320px;width:950px;height:1px;background:rgba(200,230,240,.8)}
.progress .done{position:absolute;left:0;top:-2px;width:300px;height:3px;background:#dfeff4}
.num{position:absolute;top:323px;font-size:12px;color:#e6e6e6}

.card{top:528px;width:220px;height:269px;background:var(--white);border:1px solid #e6e6e6}
.card .photo{height:146px}
.card h3{height:50px;background:var(--panel);font-weight:400;font-size:19px;text-align:center;line-height:50px;color:var(--text)}
.card.active h3{background:var(--green);color:var(--white)}
.card.active{border-bottom:4px solid var(--green-dark)}
.card p{padding:4px 18px;font-size:12px;line-height:18px;color:var(--muted)}

.rule{left:10px;top:837px;width:940px;height:1px;background:#e3e3e3}
.vrule{left:557px;top:855px;width:1px;height:410px;background:#e3e3e3}
.welcome{left:12px;top:845px;font-size:30px;font-weight:400;color:var(--text)}
.frame{left:10px;top:894px;width:540px;height:248px;border:1px solid #aaa;background:#ddd;padding:5px}
.frame div{width:100%;height:100%;background:linear-gradient(110deg,#6f6a5c,#b09a7a 45%,#8a5c3a 70%,#d8cfc0)}
.intro{left:11px;top:1148px;width:540px;font-size:18px;line-height:24px;color:var(--text)}

.formhead{left:570px;top:853px;width:380px;height:36px;background:var(--green);border:1px solid var(--green-dark);color:var(--white);font-size:20px;text-align:center;line-height:34px}
.field{height:36px;border:1px solid #999;background:var(--white);font-size:13px;color:var(--text);padding-left:13px;line-height:34px}
.field svg{position:absolute;right:10px;top:8px}
.select .btn{position:absolute;right:0;top:0;width:34px;height:34px;background:var(--green)}
.select .btn svg{right:9px;top:11px}
.delivery{left:568px;top:1130px;font-size:20px;color:var(--text)}
.submit{left:570px;top:1218px;width:200px;height:30px;background:var(--green);color:var(--white);font-size:12px;text-align:center;line-height:30px}
.submit svg{position:absolute;right:22px;top:10px}

.footer{left:0;top:1350px;width:960px;height:50px;background:var(--green);text-align:center;line-height:48px;font-size:15px;color:var(--olive)}
</style>
</head>
<body>
<div class="page">

  <div class="abs topbar">
    <svg width="16" height="16" viewBox="0 0 16 16"><path d="M3 1l3 3-2 2c1 2 3 4 6 6l2-2 3 3-2 2C7 15 1 9 1 3z" fill="#777"/></svg>
    <span>Call Us:555-010-2468 &nbsp;|&nbsp; Follow Us:</span>
    <span class="social a"></span><span class="social b"></span>
  </div>

  <nav class="abs nav">
    <a class="home">Home</a>
    <a style="left:225px">Packages &amp; Supplies</a>
    <a style="left:386px">Rent Chicken</a>
    <a style="left:498px">Services</a>
    <a style="left:577px">About</a>
    <a style="left:641px">Contact</a>
    <div class="abs search">Search...
      <svg width="17" height="17" viewBox="0 0 17 17"><circle cx="7" cy="7" r="5" fill="none" stroke="#4d5a17" stroke-width="2"/><path d="M11 11l5 5" stroke="#4d5a17" stroke-width="2.5"/></svg>
    </div>
  </nav>

  <div class="abs logo">
    <span class="dot"></span>
    <span class="name">Lease-My-Goose</span>
  </div>

  <section class="abs hero" role="img" aria-label="Dark hen standing in a grassy yard">
    <h1>Lorem ipsum dolor sit amet,<br>suscipit nec wisi tincidunt.</h1>
    <p>Lorem ipsum dolor sit amet, suscipit nec<br>wisi tincidunt.</p>
    <div class="readmore">Read More
      <svg width="9" height="14" viewBox="0 0 9 14"><path d="M1 1l6 6-6 6" fill="none" stroke="#fff" stroke-width="2"/></svg>
    </div>
    <div class="arrow l"><svg width="20" height="26" viewBox="0 0 20 26"><path d="M14 2L4 13l10 11" fill="none" stroke="#8aa82a" stroke-width="2"/></svg></div>
    <div class="arrow r"><svg width="20" height="26" viewBox="0 0 20 26"><path d="M6 2l10 11L6 24" fill="none" stroke="#8aa82a" stroke-width="2"/></svg></div>
    <div class="progress"><div class="done"></div></div>
    <span class="num" style="left:10px">1</span>
    <span class="num" style="left:340px">2</span>
    <span class="num" style="left:660px">3</span>
  </section>

  <article class="abs card active" style="left:10px">
    <div class="photo" role="img" aria-label="Fluffy yellow chicks" style="background:linear-gradient(120deg,#c98a3a,#f0c86a 50%,#a8602a)"></div>
    <h3>Hatch Your Own Chicks</h3>
    <p>Lorem ipsum dolor sit amet, nulla amet ultricies sed wisi vitae ullamcorper.</p>
  </article>
  <article class="abs card" style="left:250px">
    <div class="photo" role="img" aria-label="Black hen resting on grass" style="background:linear-gradient(120deg,#6f8a55,#2a2535 50%,#7c8f60)"></div>
    <h3>Chickens for Rent</h3>
    <p>Lorem ipsum dolor sit amet, nulla amet ultricies sed wisi vitae ullamcorper.</p>
  </article>
  <article class="abs card" style="left:490px">
    <div class="photo" role="img" aria-label="Wooden chicken coop with wire run" style="background:linear-gradient(120deg,#5d7a3c,#c8b994 45%,#9aa07a 75%,#4f6c33)"></div>
    <h3>Coop Features</h3>
    <p>Lorem ipsum dolor sit amet, nulla amet ultricies sed wisi vitae ullamcorper.</p>
  </article>
  <article class="abs card" style="left:730px">
    <div class="photo" role="img" aria-label="Box of fresh brown and white eggs" style="background:linear-gradient(120deg,#3a2018,#d98a55 45%,#f2e6da 70%,#5b3020)"></div>
    <h3>Collect Fresh Eggs</h3>
    <p>Lorem ipsum dolor sit amet, nulla amet ultricies sed wisi vitae ullamcorper.</p>
  </article>

  <div class="abs rule"></div>
  <div class="abs vrule"></div>

  <h2 class="abs welcome">Welcome To Lease My Goose</h2>
  <div class="abs frame"><div role="img" aria-label="Hen sitting with a group of young chicks"></div></div>
  <p class="abs intro">Lorem Ipsum is simply dummy text of the printing and typeset-ting industry. Lorem Ipsum has been the industry's standard dummy text ever since the 1500s, when an unknown printer took a galley of type and scrambled it to make a type specimen book. It has survived not only five centuries,</p>

  <div class="abs formhead">Order Form</div>
  <div class="abs field" style="left:570px;top:903px;width:220px">Full Name</div>
  <div class="abs field select" style="left:810px;top:903px;width:140px">Select Type
    <span class="btn"><svg width="14" height="10" viewBox="0 0 14 10"><path d="M1 1l6 6 6-6" fill="none" stroke="#222" stroke-width="2.5"/></svg></span>
  </div>
  <div class="abs field" style="left:570px;top:948px;width:380px">Address...</div>
  <div class="abs field" style="left:570px;top:993px;width:140px">City</div>
  <div class="abs field" style="left:730px;top:994px;width:220px">State</div>
  <div class="abs field" style="left:570px;top:1041px;width:140px">Zip Code</div>
  <div class="abs field" style="left:730px;top:1041px;width:220px">Phone Number</div>
  <div class="abs field" style="left:570px;top:1088px;width:380px">Email..</div>
  <div class="abs delivery">Delivery:</div>
  <div class="abs field" style="left:570px;top:1164px;width:180px">Desired delivery date:
    <svg width="20" height="20" viewBox="0 0 20 20"><rect x="2" y="4" width="16" height="14" fill="none" stroke="#444" stroke-width="2"/><rect x="2" y="4" width="16" height="4" fill="#444"/><path d="M6 1v4M14 1v4" stroke="#444" stroke-width="2"/></svg>
  </div>
  <div class="abs field" style="left:770px;top:1164px;width:180px">Desired delivery time:
    <svg width="20" height="20" viewBox="0 0 20 20"><circle cx="10" cy="10" r="8" fill="none" stroke="#444" stroke-width="2"/><path d="M10 5v5l3 2" fill="none" stroke="#444" stroke-width="2"/></svg>
  </div>
  <div class="abs submit">Make Appointment
    <svg width="7" height="10" viewBox="0 0 7 10"><path d="M1 1l4 4-4 4" fill="none" stroke="#fff" stroke-width="2"/></svg>
  </div>

  <footer class="abs footer">Copyrights © 2013 Lease My Goose.</footer>
</div>
</body>
</html>
```